Need to have a client log in screen for work orders and estimate requests.
Nice informational landing page.

Stonefield is a full service general contractor servicing apartment complexes;
maintenance of grounds and apartments - remodeling and construction.

Design Specifics: We are pretty open here. Some good examples are
www.oakhavenworks.com , pellarestates.com and www.norvo7building.com

For the site we need:
Homepage - to explain services
Roofing page
Apartment Page
Client Portal - where clients can set up accounts to set up work/estimate request that will be routed to our email

--Will need coding, plan to host site on Wordpress

Target Market(s)

Multi family, Residential and commercial clients

Industry/Entity Type

Construction

Coding

Coded - Design and coding required

Number of Pages Required

3 page

Font styles to use
Serif

Requirements
Must have
• Client portal
Nice to have
• Not sure. please advise

```html
<!DOCTYPE html>
<html lang="en">
<head>
<meta charset="utf-8">
<title>Stonefield Construction</title>
<link rel="stylesheet" href="https://fonts.googleapis.com/css2?family=Oswald:wght@400;500;700&family=Open+Sans:wght@400;600;700&display=swap">
<style>
:root{
  --red:#c4161c;
  --red-dark:#8e0f13;
  --ink:#1d1d1d;
  --text:#6f6f6f;
  --white:#ffffff;
  --night:#141414;
  --steel:#2b3138;
  --line:#d8d8d8;
}
*{box-sizing:border-box;margin:0;padding:0}
html,body{width:1200px;height:3780px;overflow:hidden}
body{font-family:"Open Sans",Arial,sans-serif;color:var(--text);background:var(--white)}
h2{font-family:"Oswald",Arial,sans-serif;font-weight:500;font-size:46px;color:var(--ink);text-transform:uppercase;letter-spacing:1px;text-align:center}
h2 .accent{color:var(--red)}
.btn{display:inline-block;background:var(--red);color:var(--white);font-family:"Oswald",Arial,sans-serif;font-size:20px;text-transform:uppercase;padding:12px 26px;letter-spacing:.5px}
.lede{font-size:15px;line-height:28px;text-align:center;color:#8a8a8a}

/* hero */
.hero{position:relative;height:660px}
.hero-photo{position:absolute;inset:0;background:linear-gradient(180deg,#dfe3e7 0%,#8f99a3 30%,#4a5560 60%,#2a3037 100%)}
.brand{position:absolute;left:0;right:0;top:230px;text-align:center;font-family:"Oswald",Arial,sans-serif;color:var(--ink)}
.brand-name{font-size:96px;font-weight:700;line-height:1;letter-spacing:4px;color:var(--ink)}
.brand-sub{font-size:42px;letter-spacing:10px;color:var(--ink);margin-top:6px}
.hero .btn{position:absolute;left:50%;transform:translateX(-50%);top:478px}
.nav{position:absolute;left:0;right:0;bottom:0;height:52px;background:#1b1b1b;display:flex;justify-content:center;gap:0}
.nav a{font-family:"Oswald",Arial,sans-serif;font-size:15px;color:#cfcfcf;text-transform:uppercase;padding:0 30px;line-height:52px;text-decoration:none}
.nav a.active{background:var(--red);color:var(--white)}

/* welcome */
.welcome{height:410px;padding-top:40px;text-align:center}
.welcome .tag{font-family:"Oswald",Arial,sans-serif;font-size:18px;color:var(--ink);margin:6px 0 18px}
.welcome .lede{width:880px;margin:0 auto 26px}

/* what we do */
.whatwedo{height:470px;position:relative;background:linear-gradient(160deg,#5a1114 0%,#3a0b0d 50%,#1a0607 100%);padding-top:36px;color:#e3caca}
.whatwedo h2{color:var(--white)}
.offer-grid{display:flex;justify-content:center;gap:70px;margin-top:46px}
.offer{width:260px;text-align:center}
.offer-icon{width:124px;height:124px;border-radius:50%;background:var(--white);margin:0 auto 24px;display:flex;align-items:center;justify-content:center}
.offer h3{font-family:"Oswald",Arial,sans-serif;font-size:22px;color:var(--red);text-transform:uppercase;font-weight:500;margin-bottom:8px}
.offer p{font-size:13px;line-height:22px}

/* testimonial */
.testimonial{height:420px;padding-top:60px;text-align:center}
.testimonial blockquote{width:820px;margin:46px auto 24px;font-size:15px;line-height:28px;color:#8a8a8a;font-style:italic}
.cite{font-size:16px;color:var(--ink)}
.cite strong{color:var(--red);font-weight:600}
.dots{margin-top:22px;display:flex;justify-content:center;gap:10px}
.dots span{width:14px;height:14px;border-radius:50%;background:#333}
.dots span.on{background:var(--red)}

/* services */
.services{height:650px;position:relative;background:linear-gradient(180deg,#1a2026 0%,#30383f 45%,#46505a 100%);padding-top:40px;color:#d4d4d4}
.services h2{color:var(--white)}
.service-grid{display:flex;justify-content:center;gap:44px;margin-top:44px}
.service{width:340px}
.service-photo{height:200px;background:linear-gradient(180deg,#b7cfe0,#8aa070)}
.service-photo.tower{background:linear-gradient(180deg,#d7dde2,#9fa8b0)}
.service h3{font-family:"Oswald",Arial,sans-serif;font-size:19px;color:var(--white);font-weight:500;text-transform:uppercase;margin:20px 0 8px}
.service p{font-size:13px;line-height:22px}
.service .btn{margin-top:22px;font-size:18px;padding:10px 24px}

/* portal */
.portal{height:280px;padding-top:36px;text-align:center}
.portal .lede{width:820px;margin:16px auto 22px}
.signup{display:flex;justify-content:center}
.signup .field{width:340px;height:48px;border:1px solid var(--line);font-size:14px;color:#999;text-align:left;padding:14px 16px}
.signup .btn{font-size:18px;padding:0 30px;line-height:48px}

/* quote */
.quote{height:472px;background:linear-gradient(180deg,#23272b 0%,#3a4047 50%,#1e2226 100%);padding-top:36px}
.quote h2{color:var(--white)}
.quote-form{display:flex;justify-content:center;gap:40px;margin-top:40px}
.quote-col{width:500px;display:flex;flex-direction:column;gap:14px}
.input{height:48px;border:1px solid rgba(255,255,255,.7);color:#eee;font-size:14px;padding:13px 16px}
.input.area{height:176px}
.quote .submit{text-align:center;margin-top:26px}

/* contact */
.contact{height:348px;background:var(--night);padding-top:30px;text-align:center;color:#cfcfcf;position:relative}
.contact h2{color:var(--white)}
.social{display:flex;justify-content:center;gap:14px;margin:34px 0 24px}
.social span{width:40px;height:40px;background:var(--red-dark)}
.social span:nth-child(2){background:var(--red)}
.contact p{font-size:14px;line-height:24px}
.footer{position:absolute;left:0;right:0;bottom:0;height:56px;line-height:56px;background:#0a0a0a;font-size:13px;color:#999}
.footer strong{color:var(--red);font-weight:600}
</style>
</head>
<body>

<header class="hero">
  <div class="hero-photo" role="img" aria-label="Low-angle photo of a glass high-rise under a cloudy sky"></div>
  <div class="brand">
    <div class="brand-name">STONEFIELD</div>
    <div class="brand-sub">CONSTRUCTION</div>
  </div>
  <a class="btn">Client Login</a>
  <nav class="nav">
    <a class="active">Home</a><a>About</a><a>Services</a><a>Roofing</a><a>Apartments</a><a>Client Portal</a><a>Contact</a>
  </nav>
</header>

<section class="welcome">
  <h2>Welcome to <span class="accent">Stonefield</span></h2>
  <div class="tag">CONSTRUCTION</div>
  <p class="lede">Lorem Ipsum is simply dummy text of the printing and typesetting industry. Lorem Ipsum has been the industry's standard dummy text ever since the 1500s, when an unknown printer took a galley of type and scrambled it to make a type specimen book. It has survived not only five centuries, but also the leap into electronic typesetting, remaining essentially unchanged. It was popularised in the 1960s with the release of Letraset sheets containing Lorem Ipsum passages.</p>
  <a class="btn">Know More</a>
</section>

<section class="whatwedo" role="img" aria-label="Dark red background photo of roof tiles">
  <h2>What <span class="accent">We Do</span></h2>
  <div class="offer-grid">
    <div class="offer">
      <div class="offer-icon"><svg width="64" height="64" viewBox="0 0 64 64"><path d="M6 34 32 12 58 34" fill="none" stroke="#c4161c" stroke-width="6"/><rect x="16" y="34" width="32" height="22" fill="#c4161c"/></svg></div>
      <h3>Roofing</h3>
      <p>Lorem Ipsum is simply dummy text of the printing and typesetting industry. Lorem Ipsum has been the industry's standard dummy text ever since the 1500s.</p>
    </div>
    <div class="offer">
      <div class="offer-icon"><svg width="64" height="64" viewBox="0 0 64 64"><rect x="10" y="14" width="20" height="42" fill="#c4161c"/><rect x="34" y="6" width="20" height="50" fill="#c4161c"/></svg></div>
      <h3>Apartments</h3>
      <p>Lorem Ipsum is simply dummy text of the printing and typesetting industry. Lorem Ipsum has been the industry's standard dummy text ever since the 1500s.</p>
    </div>
    <div class="offer">
      <div class="offer-icon"><svg width="64" height="64" viewBox="0 0 64 64"><rect x="10" y="10" width="6" height="46" fill="#c4161c"/><rect x="10" y="10" width="44" height="6" fill="#c4161c"/><rect x="30" y="34" width="22" height="22" fill="#c4161c"/></svg></div>
      <h3>Construction</h3>
      <p>Lorem Ipsum is simply dummy text of the printing and typesetting industry. Lorem Ipsum has been the industry's standard dummy text ever since the 1500s.</p>
    </div>
  </div>
</section>

<section class="testimonial">
  <h2>What Our <span class="accent">Client Say</span></h2>
  <blockquote>"Lorem Ipsum is simply dummy text of the printing and typesetting industry. Lorem Ipsum has been the industry's standard dummy text ever since the 1500s, when an unknown printer took a galley of type and scrambled"</blockquote>
  <div class="cite"><strong>- Client Name</strong> &nbsp;Something.com</div>
  <div class="dots"><span></span><span class="on"></span><span></span><span></span></div>
</section>

<section class="services" role="img" aria-label="Dusky photo of a city skyline and glass towers">
  <h2>Our <span class="accent">Services</span></h2>
  <div class="service-grid">
    <div class="service">
      <div class="service-photo" role="img" aria-label="Rendering of a single-storey house with lawn"></div>
      <h3>Maintenance of Ground and Apartments</h3>
      <p>Lorem Ipsum is simply dummy text of the printing and typesetting industry. Lorem Ipsum has been the industry's standard dummy text ever since the 1500s, when an unknown printer took a galley of type and scrambled it.</p>
      <a class="btn">Know More</a>
    </div>
    <div class="service">
      <div class="service-photo tower" role="img" aria-label="Rendering of a white apartment tower"></div>
      <h3>Remodeling and Construction</h3>
      <p>Lorem Ipsum is simply dummy text of the printing and typesetting industry. Lorem Ipsum has been the industry's standard dummy text ever since the 1500s, when an unknown printer took a galley of type and scrambled it.</p>
      <a class="btn">Know More</a>
    </div>
  </div>
</section>

<section class="portal">
  <h2>Client <span class="accent">Portal</span></h2>
  <p class="lede">"Lorem Ipsum is simply dummy text of the printing and typesetting industry. Lorem Ipsum has been the industry's standard dummy text ever since the 1500s, when an unknown printer took a galley of type and scrambled"</p>
  <div class="signup"><div class="field">Enter Your Email</div><a class="btn">Sign Up</a></div>
</section>

<section class="quote" role="img" aria-label="Dark photo of a building under construction">
  <h2>Get A <span class="accent">Free Quote</span></h2>
  <div class="quote-form">
    <div class="quote-col">
      <div class="input">Name</div>
      <div class="input">E-Mail</div>
      <div class="input">Phone</div>
    </div>
    <div class="quote-col">
      <div class="input area">Message</div>
    </div>
  </div>
  <div class="submit"><a class="btn">Contact Us</a></div>
</section>

<footer class="contact">
  <h2>Contact <span class="accent">Us</span></h2>
  <div class="social"><span></span><span></span><span></span></div>
  <p>123-456-7890 | info@stonefieldconstruction.com</p>
  <p>101, Lorem Ipsum is simple dummy text</p>
  <div class="footer">&copy;<strong>STONEFIELD CONSTRUCTION</strong> 2016 All rights reserved</div>
</footer>

</body>
</html>
```